Wordpress website update with basic ecomm features

We need an update to our existing website
www.brightmoorhub.com.au that can be easily updated, enhances our logo and can take payments online and a basic text logo suite for 3 products. Website would reflect confidence and give clients confidence in the outcomes we will provide for them. must be easy to use, crisp, fresh, clean and dynamic.

Target Market(s)

entrepreneurs, professionals, small business owners, corporate organisations, universities

Industry/Entity Type

Online

Coding

Coded - Design and coding required

Number of Pages Required

5+ page

Font styles to use
Sans Serif

Requirements
Must have
• be easy to navigate, look professional, please see brief doc
Nice to have
• please see briefing doc
Should not have
• please see briefing doc

```html
<!DOCTYPE html>
<html lang="en">
<head>
<meta charset="utf-8">
<title>Brightmoor Hub</title>
<link rel="stylesheet" href="https://fonts.googleapis.com/css2?family=Montserrat:wght@400;500;600&family=Open+Sans:wght@400;600&display=swap">
<style>
:root{
  --blue:#1ea3d6;
  --blue-dark:#1690c2;
  --ink:#222;
  --text:#555;
  --muted:#777;
  --line:#d9d9d9;
  --white:#fff;
  --band:#2fb0de;
}
*{box-sizing:border-box;margin:0;padding:0}
html,body{width:1200px;height:2659px;overflow:hidden;background:var(--white)}
body{font-family:"Open Sans",Arial,sans-serif;color:var(--text)}
.page{position:relative;width:1200px;height:2659px;overflow:hidden}
.abs{position:absolute}
.heading{font-family:"Montserrat",Arial,sans-serif}

/* header */
.site-header{left:0;top:0;width:1200px;height:106px;background:var(--white);border-bottom:1px solid #eee}
.brand{left:115px;top:27px;height:62px;display:flex;align-items:center;gap:16px}
.brand-square{width:62px;height:62px;background:#111}
.brand-name{font-family:"Montserrat",Arial,sans-serif;font-size:20px;letter-spacing:5px;color:#111;font-weight:500;text-transform:uppercase}
.main-nav a{position:absolute;top:39px;height:37px;line-height:37px;font-family:"Montserrat",Arial,sans-serif;font-size:15px;color:#333;text-decoration:none;text-transform:uppercase}
.main-nav .active{border:2px solid var(--blue);color:var(--blue);width:89px;text-align:center;left:478px}

/* hero */
.hero{left:0;top:106px;width:1200px;height:479px;background:linear-gradient(100deg,#eef3f6 0%,#e3eaee 45%,#c7d3da 70%,#dfe6ea 100%)}
.hero-title{left:124px;top:289px;width:526px;height:60px;background:rgba(255,255,255,.92);font-size:32px;color:#111;line-height:60px;padding-left:18px;font-weight:500}
.hero-sub{left:124px;top:349px;width:526px;height:44px;background:var(--blue);color:#fff;font-size:24px;line-height:44px;padding-left:18px;font-weight:500}
.dot{width:13px;height:13px;border-radius:50%;border:2px solid #333;top:552px}
.dot.fill{background:#333}

/* features */
.section-title{width:1200px;left:0;text-align:center;font-family:"Montserrat",Arial,sans-serif;color:#222;text-transform:uppercase}
.feature{width:220px;text-align:center}
.feature-ring{width:156px;height:156px;margin:0 auto;border-radius:50%;border:6px solid #ececec;display:flex;align-items:center;justify-content:center}
.feature-label{margin-top:24px;font-family:"Montserrat",Arial,sans-serif;color:var(--blue);font-size:17px;line-height:22px;text-transform:uppercase}
.feature-text{margin-top:10px;font-size:12.5px;line-height:18px;color:var(--muted)}

/* about */
.about{left:0;top:959px;width:1200px;height:349px;background:linear-gradient(90deg,#3bb8e3 0%,#2cacdc 55%,#2197c9 100%)}
.about h2{position:absolute;top:64px;width:1200px;text-align:center;color:#fff;font-size:29px;font-weight:400}
.about p{position:absolute;left:170px;top:120px;width:860px;text-align:center;color:#eaf7fd;font-size:16px;line-height:30px}
.btn-outline{position:absolute;text-align:center;font-family:"Montserrat",Arial,sans-serif;text-transform:uppercase;text-decoration:none}
.about .btn-outline{left:525px;top:232px;width:145px;height:44px;line-height:40px;border:2px solid #fff;color:#fff;font-size:14px;font-weight:600}

/* cards */
.card{top:1359px;width:307px;height:343px;border:1px solid var(--line);background:#fff}
.card-image{width:100%;height:160px}
.card h3{margin-top:20px;text-align:center;font-size:19px;font-weight:500;color:#222;text-transform:uppercase}
.card p{margin:12px 28px 0;text-align:center;font-size:12.5px;line-height:19px;color:var(--muted)}
.card .btn-outline{left:94px;top:289px;width:118px;height:32px;line-height:29px;border:1.5px solid var(--blue);color:var(--blue);font-size:12px}

/* form */
.capture{left:0;top:1778px;width:1200px;height:423px;background:linear-gradient(110deg,#e6ecef 0%,#f1f4f6 40%,#e9eef1 70%,#dde4e8 100%)}
.chevron{left:565px;top:1749px;width:64px;height:64px;border-radius:50%;background:#fff;display:flex;align-items:center;justify-content:center}
.capture-title{top:1826px;color:var(--blue);font-size:26px;font-weight:400}
.field{background:#fff;border:1px solid #d6d6d6;font-size:13px;color:#666;padding:10px 14px}
.submit{left:516px;top:2106px;width:166px;height:46px;background:linear-gradient(#28abdc,#1690c2);color:#fff;font-family:"Montserrat",Arial,sans-serif;font-size:20px;text-align:center;line-height:46px}

/* partners */
.partner{top:2253px;height:28px;background:#d6d6d6;border-radius:3px}

/* footer */
.footer-col h4{font-family:"Montserrat",Arial,sans-serif;font-size:17px;font-weight:500;color:#333;text-transform:uppercase}
.footer-col ul{list-style:none;margin-top:20px}
.footer-col li{font-size:13px;color:#555;height:25.5px}
.contact-item{left:702px;display:flex;gap:12px;font-size:13px;color:#555;line-height:19px}
.contact-icon{flex:none;width:30px;height:30px;border-radius:50%;border:1.5px solid var(--blue);display:flex;align-items:center;justify-content:center}
.social{top:2520px;width:36px;height:36px;border-radius:50%;background:var(--blue)}
.rule{left:128px;top:2597px;width:957px;height:1px;background:#cfcfcf}
.copyright{left:0;top:2614px;width:1200px;text-align:center;font-size:13px;color:#777}
</style>
</head>
<body>
<div class="page">

  <header class="site-header abs">
    <div class="brand abs">
      <span class="brand-square"></span>
      <span class="brand-name">Brightmoor Hub</span>
    </div>
    <nav class="main-nav">
      <a class="active">Home</a>
      <a style="left:596px">About us</a>
      <a style="left:720px">Features</a>
      <a style="left:842px">Testimonial</a>
      <a style="left:993px">Contact</a>
    </nav>
  </header>

  <section class="hero abs" role="img" aria-label="Photo of a smiling businessman working at a laptop with charts on his desk"></section>
  <div class="hero-title abs heading">THE EXPERIENCED ECONOMY</div>
  <div class="hero-sub abs heading">SHARED LEARNING &amp; OPPORTUNITIES</div>
  <span class="dot abs" style="left:552px"></span>
  <span class="dot abs fill" style="left:581px"></span>
  <span class="dot abs fill" style="left:611px"></span>
  <span class="dot abs fill" style="left:643px"></span>

  <h2 class="section-title abs" style="top:614px;font-size:27px;font-weight:400">Our Features</h2>

  <div class="feature abs" style="left:129px;top:675px">
    <div class="feature-ring">
      <svg width="70" height="70" viewBox="0 0 70 70" fill="none" stroke="#1ea3d6" stroke-width="3"><rect x="14" y="14" width="42" height="42" rx="4"/><path d="M22 46l10-10 8 8 10-14"/><path d="M44 30h6v6"/></svg>
    </div>
    <div class="feature-label">Commercialisation<br>Program</div>
    <p class="feature-text">Morbi diam mauris viverra in gravida eu mattis in ante Morbi</p>
  </div>
  <div class="feature abs" style="left:372px;top:675px">
    <div class="feature-ring">
      <svg width="70" height="70" viewBox="0 0 70 70" fill="none" stroke="#1ea3d6" stroke-width="3"><path d="M10 22h18l4 5h28v28H10z"/><circle cx="40" cy="42" r="9"/><path d="M40 47v-10M36 41l4-4 4 4"/></svg>
    </div>
    <div class="feature-label">Upload videos<br>and photos</div>
    <p class="feature-text">Morbi diam mauris viverra in gravida eu mattis in ante Morbi</p>
  </div>
  <div class="feature abs" style="left:618px;top:675px">
    <div class="feature-ring">
      <svg width="70" height="70" viewBox="0 0 70 70" fill="none" stroke="#1ea3d6" stroke-width="3"><path d="M12 16h14a5 5 0 0 1 10 0h14v14a5 5 0 0 1 0 10v14H36a5 5 0 0 0-10 0H12V40a5 5 0 0 0 0-10z"/><path d="M31 16v38M12 35h38"/></svg>
    </div>
    <div class="feature-label">Who are our<br>partners</div>
    <p class="feature-text">Morbi diam mauris viverra in gravida eu mattis in ante Morbi</p>
  </div>
  <div class="feature abs" style="left:861px;top:675px">
    <div class="feature-ring">
      <svg width="74" height="70" viewBox="0 0 74 70" fill="none" stroke="#1ea3d6" stroke-width="3"><ellipse cx="28" cy="30" rx="20" ry="14"/><path d="M18 42l-4 10 12-7"/><path d="M46 22c10 1 18 7 18 15 0 4-2 7-5 10l3 9-10-6c-3 1-6 1-9 1-6 0-11-2-14-5"/></svg>
    </div>
    <div class="feature-label">Book us for<br>a talk</div>
    <p class="feature-text">Morbi diam mauris viverra in gravida eu mattis in ante Morbi</p>
  </div>

  <section class="about abs">
    <h2 class="heading">ABOUT OUR COMPANY</h2>
    <p>Brightmoor Hub builds and develops validation and innovation programs, communities and data to improve the overall success rate of entrepreneurial and early-stage ventures. Our aim is to build a flourishing innovation and collaboration eco-system that validates people, business &amp; society.</p>
    <a class="btn-outline">Read more</a>
  </section>

  <article class="card abs" style="left:117px">
    <div class="card-image" role="img" aria-label="Photo of a team gathered around a laptop" style="background:linear-gradient(135deg,#b9c6d2,#7d8fa1 60%,#a4b3c0)"></div>
    <h3 class="heading">Why Brightmoor Hub</h3>
    <p>Morbi porta libero id ullamcorper nonummy nibh ligula pulvinar metus eget consectetuer augue nisi quis lacus Ut ac</p>
    <a class="btn-outline">Read more</a>
  </article>
  <article class="card abs" style="left:445px">
    <div class="card-image" role="img" aria-label="Photo of two colleagues working together at a desk" style="background:linear-gradient(135deg,#e3e7ea,#b7c0c8 60%,#d3d9de)"></div>
    <h3 class="heading">Outline of program</h3>
    <p>Morbi porta libero id ullamcorper nonummy nibh ligula pulvinar metus eget consectetuer augue nisi quis lacus Ut ac</p>
    <a class="btn-outline">Read more</a>
  </article>
  <article class="card abs" style="left:775px">
    <div class="card-image" role="img" aria-label="Photo of a handshake over a city skyline" style="background:linear-gradient(160deg,#8ea6c6,#3f5676 55%,#6c7f99)"></div>
    <h3 class="heading">What we deliver</h3>
    <p>Morbi porta libero id ullamcorper nonummy nibh ligula pulvinar metus eget consectetuer augue nisi quis lacus Ut ac</p>
    <a class="btn-outline">Read more</a>
  </article>

  <section class="capture abs" role="img" aria-label="Faded photo of hands typing on a keyboard"></section>
  <div class="chevron abs">
    <svg width="24" height="14" viewBox="0 0 24 14" fill="none" stroke="#1ea3d6" stroke-width="3"><path d="M2 2l10 10 10-10"/></svg>
  </div>
  <h2 class="section-title capture-title abs">Need to capture data</h2>
  <div class="field abs" style="left:184px;top:1882px;width:412px;height:41px">Your Name</div>
  <div class="field abs" style="left:606px;top:1882px;width:413px;height:41px">Email address</div>
  <div class="field abs" style="left:184px;top:1932px;width:412px;height:41px">Phone</div>
  <div class="field abs" style="left:606px;top:1932px;width:413px;height:41px">Location</div>
  <div class="field abs" style="left:184px;top:1985px;width:835px;height:103px">Message</div>
  <div class="submit abs">SUBMIT</div>

  <div class="partner abs" style="left:140px;width:64px"></div>
  <div class="partner abs" style="left:258px;width:108px"></div>
  <div class="partner abs" style="left:424px;width:90px"></div>
  <div class="partner abs" style="left:582px;width:104px"></div>
  <div class="partner abs" style="left:768px;width:80px"></div>
  <div class="partner abs" style="left:917px;width:112px"></div>

  <div class="footer-col abs" style="left:135px;top:2348px">
    <h4>Company</h4>
    <ul><li>Home</li><li>About</li><li>What we do</li><li>Team</li></ul>
  </div>
  <div class="footer-col abs" style="left:312px;top:2348px">
    <h4>Services</h4>
    <ul><li>Outline of program</li><li>What we deliver</li><li>Outcomes</li><li>Upload videos and photos</li></ul>
  </div>
  <div class="footer-col abs" style="left:525px;top:2348px">
    <h4>Resources</h4>
    <ul><li>Team</li><li>Support</li><li>FAQ</li><li>Contact</li></ul>
  </div>
  <div class="footer-col abs" style="left:702px;top:2348px">
    <h4>Contact us</h4>
  </div>
  <div class="contact-item abs" style="top:2392px">
    <span class="contact-icon"><svg width="14" height="16" viewBox="0 0 14 16" fill="#1ea3d6"><path d="M7 0a6 6 0 0 0-6 6c0 4.5 6 10 6 10s6-5.5 6-10a6 6 0 0 0-6-6zm0 8.5A2.5 2.5 0 1 1 7 3.5a2.5 2.5 0 0 1 0 5z"/></svg></span>
    <span>Alder Court, 14 Wrenfield Lane, Harlow Vale,<br>HV3 2LT, United Kingdom</span>
  </div>
  <div class="contact-item abs" style="top:2442px;align-items:center">
    <span class="contact-icon"><svg width="14" height="14" viewBox="0 0 14 14" fill="#1ea3d6"><path d="M3 0l2.5 3.5L4 5.5c1 2 2.5 3.5 4.5 4.5l2-1.5L14 11l-1.5 2.5C6 13.5.5 8 .5 1.5z"/></svg></span>
    <span>+44 (0) 7700 900418</span>
  </div>
  <div class="contact-item abs" style="top:2475px;align-items:center">
    <span class="contact-icon"><svg width="14" height="10" viewBox="0 0 14 10" fill="none" stroke="#1ea3d6" stroke-width="1.5"><rect x=".75" y=".75" width="12.5" height="8.5"/><path d="M1 1l6 5 6-5"/></svg></span>
    <span>hello@brightmoorhub.com</span>
  </div>
  <span class="social abs" style="left:705px"></span>
  <span class="social abs" style="left:751px"></span>
  <span class="social abs" style="left:799px"></span>
  <span class="social abs" style="left:847px"></span>

  <div class="rule abs"></div>
  <p class="copyright abs">© 2016 Company Name &nbsp;All right reserved</p>

</div>
</body>
</html>
```